Australian Software Consultancy needs new Business Card Design

Design Business Card based on existing design artefacts (attached). We are open to all designs. As its a 2 sided design and we thought it might be quite striking to have one side with a black background and te other side with a white background.

Target Market(s)

Financial Services mainly.

Industry/Entity Type

Business

Contact Information for Business Card

Requirements
Must have
• Funky design using our existing assets

```html
<!DOCTYPE html>
<html lang="en">
<head>
<meta charset="utf-8">
<title>Keen Harbor – Business Card</title>
<link href="https://fonts.googleapis.com/css2?family=Montserrat:wght@500;600;700;800&display=swap" rel="stylesheet">
<style>
  :root {
    --backdrop: #2e2c35;
    --card-white: #ffffff;
    --card-black: #000000;
    --brand-red: #d6323e;
    --ink: #1a1a1a;
    --ink-soft: #555555;
    --paper-text: #ffffff;
  }
  * { box-sizing: border-box; margin: 0; padding: 0; }
  html, body {
    width: 1200px; height: 1173px; overflow: hidden;
    background: var(--backdrop);
    font-family: "Montserrat", sans-serif;
  }
  .stage {
    width: 1200px; height: 1173px;
    display: flex; flex-direction: column; align-items: center; justify-content: center;
    gap: 60px;
  }
  .card {
    position: relative;
    width: 840px; height: 480px;
    overflow: hidden;
    box-shadow: 0 18px 40px rgba(0,0,0,0.45);
  }

  /* ---------- Front (white) ---------- */
  .card--front { background: var(--card-white); }
  .front-brand {
    position: absolute; left: 90px; top: 150px;
    display: flex; align-items: center; gap: 22px;
  }
  .brand-ring {
    width: 150px; height: 150px; border-radius: 50%;
    border: 14px solid var(--brand-red);
  }
  .front-brand .brand-name {
    font-weight: 700; font-size: 30px; color: var(--brand-red);
    text-transform: uppercase; letter-spacing: 1px; line-height: 1.1;
  }
  .contact-block {
    position: absolute; left: 500px; top: 110px;
  }
  .person-name {
    font-weight: 700; font-size: 38px; color: var(--brand-red); line-height: 1;
  }
  .person-title {
    font-weight: 600; font-size: 18px; color: var(--ink); margin-top: 6px;
  }
  .contact-list { list-style: none; margin-top: 28px; display: grid; gap: 16px; }
  .contact-item {
    display: flex; align-items: center; gap: 16px;
    font-weight: 500; font-size: 19px; color: var(--ink-soft);
  }
  .contact-icon {
    width: 34px; height: 34px; border-radius: 50%;
    background: var(--brand-red);
    display: flex; align-items: center; justify-content: center;
  }
  .contact-icon svg { width: 18px; height: 18px; }

  /* ---------- Back (black) ---------- */
  .card--back { background: var(--card-black); }
  .back-ring {
    position: absolute; left: 50%; top: 40px; transform: translateX(-50%);
    width: 190px; height: 190px; border-radius: 50%;
    border: 14px solid var(--brand-red);
  }
  .back-name {
    position: absolute; left: 0; right: 0; top: 265px;
    text-align: center;
    font-weight: 800; font-size: 66px; letter-spacing: 2px;
    color: var(--paper-text); text-transform: uppercase;
  }
  .back-swoosh { position: absolute; left: 0; bottom: 0; width: 840px; height: 140px; }
</style>
</head>
<body>
<main class="stage">

  <section class="card card--front" aria-label="Card front">
    <div class="front-brand">
      <div class="brand-ring" aria-hidden="true"></div>
      <div class="brand-name">Keen<br>Harbor</div>
    </div>

    <div class="contact-block">
      <h1 class="person-name">Name</h1>
      <p class="person-title">Job Title</p>
      <ul class="contact-list">
        <li class="contact-item">
          <span class="contact-icon">
            <svg viewBox="0 0 24 24" fill="#fff"><path d="M6.6 10.8a15.1 15.1 0 0 0 6.6 6.6l2.2-2.2c.3-.3.7-.4 1-.2 1.1.4 2.3.6 3.6.6.6 0 1 .4 1 1V20c0 .6-.4 1-1 1A17 17 0 0 1 3 4c0-.6.4-1 1-1h3.5c.6 0 1 .4 1 1 0 1.3.2 2.5.6 3.6.1.3 0 .7-.2 1z"/></svg>
          </span>Phone
        </li>
        <li class="contact-item">
          <span class="contact-icon">
            <svg viewBox="0 0 24 24" fill="none" stroke="#fff" stroke-width="2"><rect x="3" y="6" width="18" height="12"/><path d="M3 6l9 7 9-7"/></svg>
          </span>Email
        </li>
        <li class="contact-item">
          <span class="contact-icon">
            <svg viewBox="0 0 24 24" fill="none" stroke="#fff" stroke-width="2"><circle cx="12" cy="12" r="9"/><path d="M3 12h18M12 3c3 3 3 15 0 18M12 3c-3 3-3 15 0 18"/></svg>
          </span>Website
        </li>
        <li class="contact-item">
          <span class="contact-icon">
            <svg viewBox="0 0 24 24" fill="#fff"><path d="M12 3l9 8h-3v9h-4v-6h-4v6H6v-9H3z"/></svg>
          </span>Address
        </li>
      </ul>
    </div>
  </section>

  <section class="card card--back" aria-label="Card back">
    <div class="back-ring" aria-hidden="true"></div>
    <div class="back-name">Keen Harbor</div>
    <svg class="back-swoosh" viewBox="0 0 840 140" preserveAspectRatio="none" aria-hidden="true">
      <path d="M0 90 Q 480 70 840 0 L840 140 L0 140 Z" fill="var(--brand-red)"/>
    </svg>
  </section>

</main>
</body>
</html>
```